Shavers of the Fernbrook Business Card

We need a clean but professional business card design for a men's grooming barber shop. Our demographic is for the professional male so it needs to be esthetically pleasing and interesting to that demographic. Our website has a leather background and we have hardwood flooring in the shop so either of those two could work on the card.
I would not be apposed to a slightly different shape business card than usual, like a square.
The final design should be clean, clear, and call out to all male professionals looking for a guys place to get a cut and a shave and relax with a cigar.
Target Market(s)
Professional Male ages between 25 -50
Industry/Entity Type
Business
Requirements
Must have
- My logo and be visible. I designed myself some referral cards and i need to make the background of my logo have a white dropshadow.

```html
<!DOCTYPE html>
<html lang="en">
<head>
<meta charset="utf-8">
<title>Shavers of the Fernbrook — Business Card</title>
<link href="https://fonts.googleapis.com/css2?family=Cutive&display=swap" rel="stylesheet">
<style>
  :root {
    --page: #e8e5de;
    --front-light: #918678;
    --front-dark: #6c6359;
    --back-light: #4a4a4a;
    --back-dark: #2e2e2e;
    --ink: #141414;
    --paper: #e4e4e2;
    --rule: #6a6a6a;
  }
  * { box-sizing: border-box; margin: 0; padding: 0; }
  html, body {
    width: 1200px; height: 1001px; overflow: hidden;
    background: var(--page);
    font-family: "Cutive", "Courier New", serif;
    color: var(--ink);
  }
  .sheet {
    position: relative; width: 1200px; height: 1001px;
  }
  .card {
    position: absolute; top: 250px;
    width: 500px; height: 500px;
    border-radius: 44px;
    box-shadow: 0 6px 18px rgba(0,0,0,0.18);
  }
  .card-front {
    left: 70px;
    background: radial-gradient(circle at 40% 30%, var(--front-light), var(--front-dark));
  }
  .card-back {
    left: 630px;
    background: radial-gradient(circle at 40% 30%, var(--back-light), var(--back-dark));
  }
  .brand {
    position: absolute; top: 90px; left: 0; right: 0;
    display: flex; flex-direction: column; align-items: center; gap: 14px;
  }
  .brand-mark {
    width: 22px; height: 22px; border-radius: 50%;
    background: var(--ink);
  }
  .brand-name {
    font-size: 34px; line-height: 1.2; text-align: center;
    text-transform: uppercase; letter-spacing: 1px;
  }
  .contact {
    position: absolute; left: 60px; bottom: 62px;
    display: flex; align-items: center; gap: 26px;
  }
  .pole {
    width: 30px; height: 108px; border-radius: 8px;
    background: linear-gradient(180deg, #2a2a2a, #555 50%, #2a2a2a);
  }
  .address {
    font-size: 22px; line-height: 1.2; text-transform: uppercase;
  }
  .appointment {
    position: absolute; left: 110px; top: 100px;
    width: 280px; height: 200px;
    background: var(--paper);
    border: 4px solid var(--ink);
    padding: 30px 22px;
  }
  .appointment-title { font-size: 17px; text-transform: uppercase; margin-bottom: 26px; }
  .field {
    font-size: 16px; text-transform: uppercase;
    border-bottom: 1px solid var(--rule);
    padding-bottom: 2px; margin: 0 0 22px 10px;
  }
</style>
</head>
<body>
<main class="sheet">
  <section class="card card-front">
    <div class="brand">
      <span class="brand-mark"></span>
      <p class="brand-name">Shavers of<br>the Fernbrook</p>
    </div>
    <div class="contact">
      <div class="pole" role="img" aria-label="Striped barber pole icon"></div>
      <p class="address">42 Marsh Hollow Lane,<br>Suite C<br>Fernbrook, SC 29000<br>Phone 555.014.2270</p>
    </div>
  </section>
  <section class="card card-back">
    <div class="appointment">
      <p class="appointment-title">Next Appointment:</p>
      <p class="field">Date</p>
      <p class="field">Time</p>
    </div>
  </section>
</main>
</body>
</html>
```